Business Card Revision

Need to redesign my business cards for a new professional look. We are a courier company. You can go to www.qvrunners.com to see what we do. The trucks have an old company name (Sprout) on them but that is the company we are just now
changing the name.

Target Market(s)

Potential clients. We service the automotive, plumbing, printing, air freight industries as well as many others.

Industry/Entity Type

Business

Contact Information for Business Card

QVmotion
20864 Lark Fenmore Parkway
Cincinnati, Oh 45873

Thomas R. Wendall
President

tom@qvrunners.com

Main: (513) 555-0147

```html
<!DOCTYPE html>
<html lang="en">
<head>
<meta charset="utf-8">
<title>QVmotion Business Card</title>
<link href="https://fonts.googleapis.com/css2?family=Lato:wght@400;700;900&display=swap" rel="stylesheet">
<style>
  :root {
    --backdrop: #8f8f8f;
    --paper: #ffffff;
    --brand-blue: #1b75bc;
    --back-blue: #088bd4;
    --charcoal: #333333;
    --accent-green: #39b54a;
    --ink-light: #ffffff;
  }
  * { margin: 0; padding: 0; box-sizing: border-box; }
  html, body {
    width: 1200px;
    height: 910px;
    overflow: hidden;
    background: var(--backdrop);
    font-family: "Lato", sans-serif;
  }
  .business-card {
    position: absolute;
    width: 700px;
    height: 400px;
    overflow: hidden;
    box-shadow: 0 4px 12px rgba(0,0,0,0.25);
  }
  .card-back { left: 60px; top: 40px; background: var(--back-blue); }
  .card-front { left: 440px; top: 470px; background: var(--paper); }
  .card-panels {
    position: absolute;
    inset: 0;
    width: 700px;
    height: 400px;
  }
  .panel-contact, .panel-corner { fill: var(--charcoal); }
  .panel-name { fill: var(--brand-blue); }

  .brand-lockup {
    position: absolute;
    display: flex;
    align-items: center;
    gap: 14px;
  }
  .brand-mark { width: 28px; height: 28px; }
  .brand-name {
    font-weight: 900;
    font-size: 42px;
    letter-spacing: 1px;
    line-height: 1;
  }
  .card-front .brand-lockup { left: 74px; top: 78px; }
  .card-front .brand-mark { background: var(--accent-green); }
  .card-front .brand-name { color: var(--brand-blue); }
  .card-back .brand-lockup { left: 70px; top: 70px; }
  .card-back .brand-mark { background: var(--ink-light); }
  .card-back .brand-name { color: var(--ink-light); font-size: 48px; }

  .contact-block {
    position: absolute;
    left: 80px;
    top: 234px;
    color: var(--ink-light);
  }
  .address {
    font-weight: 700;
    font-size: 19px;
    line-height: 1.15;
    font-style: normal;
  }
  .contact-lines {
    margin-top: 16px;
    font-size: 17px;
    line-height: 1.3;
  }
  .contact-row { display: flex; }
  .contact-label {
    width: 76px;
    font-weight: 700;
    color: var(--accent-green);
  }
  .contact-label span { color: var(--ink-light); font-weight: 400; }
  .name-block {
    position: absolute;
    right: 58px;
    top: 246px;
    text-align: right;
    color: var(--ink-light);
  }
  .person-name { font-weight: 700; font-size: 19px; line-height: 1.1; }
  .person-title { font-weight: 400; font-size: 15px; line-height: 1.1; }
</style>
</head>
<body>
  <div class="business-card card-back">
    <svg class="card-panels" viewBox="0 0 700 400" aria-hidden="true">
      <polygon class="panel-corner" points="330,400 700,400 700,215"/>
    </svg>
    <div class="brand-lockup">
      <div class="brand-mark"></div>
      <div class="brand-name">QVmotion</div>
    </div>
  </div>

  <div class="business-card card-front">
    <svg class="card-panels" viewBox="0 0 700 400" aria-hidden="true">
      <polygon class="panel-contact" points="0,188 360,188 495,400 0,400"/>
      <polygon class="panel-name" points="370,188 700,188 700,400 505,400"/>
    </svg>

    <div class="brand-lockup">
      <div class="brand-mark"></div>
      <div class="brand-name">QVmotion</div>
    </div>

    <div class="contact-block">
      <address class="address">20864 Lark Fenmore Parkway<br>Cincinnati, Oh 45873</address>
      <div class="contact-lines">
        <div class="contact-row"><span class="contact-label">mobile<span>:</span></span><span>(513) 555-0147</span></div>
        <div class="contact-row"><span class="contact-label">mail <span>&nbsp;&nbsp;:</span></span><span>tom@qvrunners.com</span></div>
      </div>
    </div>

    <div class="name-block">
      <div class="person-name">Thomas R. Wendall</div>
      <div class="person-title">President</div>
    </div>
  </div>
</body>
</html>
```